2in1 Bartender & Sommelier needs a business card

I need a business card. I worked as a bartender in many places but I just finished a sommelier school and I would like a new business card. I like minimal design, natural materials and something what makes the people think :) I try to be creative in cocktail making, like little mixology, little twist on recipes... I like to travel and discover new places, cultures and of course interesting drinks and improve continously...live a little bit crazy life. And I like what I do...

Target Market(s)

restaurant/winebar managers, winemakers, other sommeliers and bartenders, people who work in food and beverage sector

Industry/Entity Type

Hospitality

Contact Information for Business Card

Réka Fodor
Bartender & Sommelier
Phone: (FR) +33 6 4720 3917
(HU) +36 70 518 6092

Font styles to use
Script

Requirements
Must have
• Some sign, I am a bartender and sommelier as well.
Nice to have
• black and white maybe with 1 or 2 extra color
Should not have
• very colourful, to many things on the card

```html
<!DOCTYPE html>
<html lang="en">
<head>
<meta charset="utf-8">
<title>Réka Fodor – Business Card</title>
<link href="https://fonts.googleapis.com/css2?family=Dancing+Script:wght@700&family=Questrial&display=block" rel="stylesheet">
<style>
  :root {
    --bg: #2f4048;
    --paper: #ffffff;
    --ink-dark: #0a0b0f;
    --accent: #4b55a6;
    --accent-deep: #2f3880;
    --rule: #2c5d9a;
    --subtitle: #3b1818;
    --contact: #e9ebf2;
  }
  * { margin: 0; padding: 0; box-sizing: border-box; }
  html, body { width: 1200px; height: 900px; overflow: hidden; }
  body {
    background: var(--bg);
    display: flex;
    flex-direction: column;
    align-items: center;
    justify-content: center;
    gap: 44px;
  }
  .card {
    width: 680px;
    height: 388px;
    position: relative;
    background: var(--paper);
    box-shadow: 0 10px 26px rgba(0,0,0,.35);
  }
  .identity {
    position: absolute;
    display: flex;
    flex-direction: column;
    align-items: center;
    line-height: 1;
  }
  .identity .trade-sign {
    width: 44px;
    height: 30px;
    margin-bottom: 6px;
  }
  .identity .name {
    font-family: "Dancing Script", "Brush Script MT", cursive;
    font-weight: 700;
    color: var(--accent);
    font-size: 62px;
    white-space: nowrap;
  }
  .identity .role {
    font-family: "Questrial", sans-serif;
    color: var(--subtitle);
    font-size: 21px;
    letter-spacing: .5px;
    margin-top: 2px;
    white-space: nowrap;
  }
  .card-front .identity { left: 0; right: 0; top: 92px; }
  .card-back .identity { left: 0; width: 360px; top: 124px; }
  .card-back .identity .name { font-size: 54px; }
  .card-back .identity .role { font-size: 19px; }
  .contact-panel {
    position: absolute;
    left: 360px; top: 0; right: 0; bottom: 0;
    background: var(--ink-dark);
    display: flex;
    flex-direction: column;
  }
  .contact-row {
    flex: 1;
    display: flex;
    align-items: center;
    position: relative;
    border-bottom: 1px solid var(--rule);
  }
  .contact-row:last-child { border-bottom: none; }
  .contact-row .tab {
    position: absolute;
    left: -12px;
    top: 50%;
    transform: translateY(-60%);
    width: 50px;
    height: 46px;
  }
  .contact-row .text {
    margin-left: 62px;
    font-family: "Questrial", sans-serif;
    color: var(--contact);
    font-size: 20px;
    letter-spacing: 1px;
  }
</style>
</head>
<body>

  <section class="card card-front">
    <div class="identity">
      <svg class="trade-sign" viewBox="0 0 44 30" role="img" aria-label="Wine glass and cocktail glass sign">
        <g fill="none" stroke="var(--accent)" stroke-width="1.6" stroke-linecap="round">
          <path d="M6 2 H16 Q17 12 11 14 Q5 12 6 2 Z"/>
          <path d="M11 14 V26 M7 27 H15"/>
          <path d="M26 3 H40 L33 13 Z"/>
          <path d="M33 13 V26 M29 27 H37"/>
        </g>
      </svg>
      <span class="name">Réka Fodor</span>
      <span class="role">Bartender &amp; Sommelier</span>
    </div>
  </section>

  <section class="card card-back">
    <div class="identity">
      <svg class="trade-sign" viewBox="0 0 44 30" role="img" aria-label="Wine glass and cocktail glass sign">
        <g fill="none" stroke="var(--accent)" stroke-width="1.6" stroke-linecap="round">
          <path d="M6 2 H16 Q17 12 11 14 Q5 12 6 2 Z"/>
          <path d="M11 14 V26 M7 27 H15"/>
          <path d="M26 3 H40 L33 13 Z"/>
          <path d="M33 13 V26 M29 27 H37"/>
        </g>
      </svg>
      <span class="name">Réka Fodor</span>
      <span class="role">Bartender &amp; Sommelier</span>
    </div>

    <div class="contact-panel">
      <div class="contact-row">
        <svg class="tab" viewBox="0 0 50 46" aria-hidden="true">
          <path d="M0 30 Q0 46 12 46 L12 30 Z" fill="var(--accent-deep)"/>
          <rect x="0" y="0" width="50" height="32" fill="var(--accent)"/>
          <path d="M17 13 q8-6 16 0 l-2 3 h-3 l-1-2 h-4 l-1 2 h-3 z" fill="#fff"/>
          <rect x="18" y="17" width="14" height="8" rx="1" fill="#fff"/>
          <circle cx="25" cy="21" r="2" fill="var(--accent)"/>
        </svg>
        <span class="text">+33 6 4720 3917</span>
      </div>
      <div class="contact-row">
        <svg class="tab" viewBox="0 0 50 46" aria-hidden="true">
          <path d="M0 30 Q0 46 12 46 L12 30 Z" fill="var(--accent-deep)"/>
          <rect x="0" y="0" width="50" height="32" fill="var(--accent)"/>
          <rect x="19" y="5" width="12" height="22" rx="2" fill="#fff"/>
          <rect x="21" y="8" width="8" height="6" fill="var(--accent)"/>
          <g fill="var(--accent)">
            <rect x="21" y="17" width="2" height="2"/><rect x="24" y="17" width="2" height="2"/><rect x="27" y="17" width="2" height="2"/>
            <rect x="21" y="21" width="2" height="2"/><rect x="24" y="21" width="2" height="2"/><rect x="27" y="21" width="2" height="2"/>
          </g>
        </svg>
        <span class="text">+36 70 518 6092</span>
      </div>
      <div class="contact-row">
        <svg class="tab" viewBox="0 0 50 46" aria-hidden="true">
          <path d="M0 30 Q0 46 12 46 L12 30 Z" fill="var(--accent-deep)"/>
          <rect x="0" y="0" width="50" height="32" fill="var(--accent)"/>
          <path d="M15 13 L25 6 L35 13 V26 H15 Z" fill="#fff"/>
          <circle cx="25" cy="17" r="4" fill="none" stroke="var(--accent)" stroke-width="1.6"/>
          <circle cx="25" cy="17" r="1.5" fill="var(--accent)"/>
        </svg>
        <span class="text">info@your.com</span>
      </div>
      <div class="contact-row">
        <svg class="tab" viewBox="0 0 50 46" aria-hidden="true">
          <path d="M0 30 Q0 46 12 46 L12 30 Z" fill="var(--accent-deep)"/>
          <rect x="0" y="0" width="50" height="32" fill="var(--accent)"/>
          <circle cx="25" cy="16" r="10" fill="#fff"/>
          <path d="M15 16 H35 M25 6 V26" stroke="var(--accent)" stroke-width="1.4"/>
          <ellipse cx="25" cy="16" rx="4.5" ry="10" fill="none" stroke="var(--accent)" stroke-width="1.4"/>
        </svg>
        <span class="text">www.yourdomain.com</span>
      </div>
    </div>
  </section>

</body>
</html>
```